HomePage Design for Lumen Getaways - once-in-a-lifetime experiences for busy working people

Design a homepage for the Lumen Getaways (www.lumengetaways.example) website compatible with further web pages and the design briefing documents attached

LG HomePage Design Brief
We are seeking website HomePage designs incorporating our new Logo and colour scheme, for Lumen Getaways (www.lumengetaways.example) to go with the site functionality and wireframe ideas attached.
The website HomePage design needs to
• Incorporate and be consistent with the LG Logo and its colour scheme attached.
• Express the brand values of being inspirational, high quality, upscale, cultured, aspirational, and contemporary – even somewhat ‘hip’. Probably positioned somewhere between Harlow Pike (Deluxe Travel) and Green Walrus (Hip Travel) – see https://www.harlowpike.example and https://www.greenwalrus.example .
• Be instantly recognisable and different from other travel websites and instantly communicate the nature of the brand proposition and target customer base.
• Appeal to our core 25-55 affluent businesspeople demographic
• Work in the UK, US/Canada and Australia/NZ and ultimately in mainland Europe.
• Use fonts and colours that are easily reproduced online and compatible with nearly all browsers.
• Be part of a responsive website design, that can be used both on Desktops and laptops but also with tablets and mobile ‘phones (hence content not too wide across the page)
• Feature the strapline ‘Lumen Getaways in less than 7 Days’
• Work with the and wireframes and processes shown in the attached presentation – although intended as a guide only these features and processes all need to be incorporated into the HomePage.
• Make full use of high quality images and video to convey our brand proposition and products

Target Market(s)

25-55 affluent businesspeople

Industry/Entity Type

Travel Industry

Number of Pages Required

1 page

Font styles to use
Sans Serif

Colors
0455a3
00a88f

Requirements
Must have
• • Incorporate and be consistent with the LG Logo and its colour scheme attached.
• • Express the brand values of being inspirational, high quality, upscale, cultured, aspirational, and contemporary – even somewhat ‘hip’. Probably positioned somewhere between Harlow Pike (Deluxe Travel) and Green Walrus (Hip Travel) – see https://www.harlowpike.example and https://www.greenwalrus.example .
• • Be instantly recognisable and different from other travel websites and instantly communicate the nature of the brand proposition and target customer base.
• • Appeal to our core 25-55 affluent businesspeople demographic
• • Be part of a responsive website design, that can be used both on Desktops and laptops but also with tablets and mobile ‘phones (hence content not too wide across the page)
• • Feature the strapline ‘Lumen Getaways in less than 7 Days’
• • Work with the and wireframes and processes shown in the attached presentation – although intended as a guide only these features and processes all need to be incorporated into the HomePage.
• • Make full use of high quality images and video to convey our brand proposition and products
• Colours as per Logo not as shown below
Nice to have
• • Work in the UK, US/Canada and Australia/NZ and ultimately in mainland Europe.
Should not have
• Must not be cheap or mass-market, nor excessively "stuffy or luxury-orientated"

```html
<!DOCTYPE html>
<html lang="en">
<head>
<meta charset="utf-8">
<title>Lumen Getaways — Homepage</title>
<link href="https://fonts.googleapis.com/css2?family=Roboto:wght@300;400;500;700&display=swap" rel="stylesheet">
<style>
:root{
  --navy:#1d2a6b;
  --brand-blue:#0455a3;
  --brand-teal:#00a88f;
  --orange:#f47a20;
  --ink:#2b2b2b;
  --muted:#777;
  --line:#d9d9d9;
  --panel:#dedfe1;
  --band:#f4f4f4;
  --foot-band:#ececec;
  --foot-dark:#2c3348;
  --white:#fff;
}
*{box-sizing:border-box;margin:0;padding:0}
html,body{width:1200px;height:2719px;overflow:hidden}
body{font-family:'Roboto',Arial,sans-serif;color:var(--ink);background:var(--white)}
.page{position:relative;width:1200px;height:2719px;overflow:hidden}
.abs{position:absolute}

/* header */
.header{left:0;top:0;width:1200px;height:94px;border-bottom:1px solid var(--line)}
.call{left:161px;top:32px;font-size:19px;font-weight:400;letter-spacing:.3px}
.mail{left:161px;top:67px;font-size:11px}
.brand{left:0;top:22px;width:1200px;text-align:center}
.brand-mark{display:inline-block;width:34px;height:34px;border-radius:50%;background:var(--brand-teal)}
.brand-name{display:block;margin-top:4px;font-size:14px;font-weight:700;color:var(--brand-blue);letter-spacing:.5px}
.search{left:1022px;top:10px}
.login{left:994px;top:34px;font-size:10px}
.socials{left:917px;top:64px;display:flex;gap:12px}
.socials span{width:12px;height:12px;border-radius:50%;background:#8a8a8a}

/* nav */
.nav{left:0;top:95px;width:1200px;height:37px;border-bottom:1px solid var(--line);display:flex;justify-content:center;align-items:center;gap:36px;font-size:12px;color:#333;letter-spacing:.3px}
.nav .caret::after{content:"";display:inline-block;margin-left:5px;width:5px;height:5px;border-right:1.3px solid #333;border-bottom:1.3px solid #333;transform:rotate(45deg) translateY(-3px)}

/* hero */
.hero{left:0;top:132px;width:1200px;height:475px;background:linear-gradient(180deg,#2c2f33 0%,#4a4f55 35%,#6b7c88 58%,#3a3d40 78%,#1e1f21 100%)}
.hero-title{left:0;top:245px;width:1200px;text-align:center;color:var(--white);font-size:35px;font-weight:300}
.hero-title b{font-weight:700}
.hero-sub{left:0;top:312px;width:1200px;text-align:center;color:var(--white);font-size:22px;font-weight:700}
.hero-btn{left:504px;top:377px;width:199px;height:38px;background:var(--orange);color:var(--white);font-size:17px;display:flex;align-items:center;justify-content:center}

/* intro */
.intro-kicker{left:0;top:650px;width:1200px;text-align:center;font-size:18px;letter-spacing:2px;color:#333}
.intro-title{left:0;top:695px;width:1200px;text-align:center;font-size:23px;font-weight:700;color:var(--navy);letter-spacing:.3px}
.intro-text{left:180px;top:734px;width:840px;text-align:center;font-size:13px;line-height:22px;color:var(--muted)}
.intro-down{left:589px;top:801px;width:22px;height:22px;border:1px solid #555;border-radius:50%;display:flex;align-items:center;justify-content:center}

/* experience grid */
.tile{width:200px}
.tile-img{width:200px;height:138px}
.tile-cap{margin-top:8px;text-align:center;line-height:15px}
.tile-cap small{display:block;font-size:11px;color:var(--muted)}
.tile-cap span{display:block;font-size:13px;color:#333}

/* video feature */
.feature-band{left:0;top:1432px;width:1200px;height:303px;background:var(--band)}
.feature{left:161px;top:1285px;width:878px;height:384px;background:var(--panel)}
.feature-title{left:196px;top:1422px;font-size:17px;color:#333;letter-spacing:.3px}
.feature-text{left:196px;top:1460px;width:300px;font-size:13px;line-height:23px;color:#444}
.video{left:542px;top:1318px;width:464px;height:315px;border:3px solid var(--white);background:linear-gradient(180deg,#9cb9d4 0%,#cfdde8 25%,#2f8fae 45%,#16708f 75%,#0f5a78 100%)}
.play{left:745px;top:1446px}
.dots{left:0;top:1689px;width:1200px;display:flex;justify-content:center;gap:4px}
.dots span{width:8px;height:8px;border-radius:50%;background:var(--foot-dark)}
.dots span.on{background:var(--orange)}

/* offers */
.offers-title{left:0;top:1780px;width:1200px;text-align:center;font-size:18px;letter-spacing:2px;color:#333}
.offer{top:1843px;width:278px;height:276px}
.offer-frame{position:absolute;left:14px;top:14px;width:250px;height:248px;border:1px solid rgba(255,255,255,.85);text-align:center;color:var(--white)}
.offer-frame h3{margin-top:12px;font-size:23px;font-weight:700}
.offer-frame p{margin-top:4px;font-size:16px;font-weight:700}
.offer-btn{position:absolute;left:53px;top:181px;width:140px;height:37px;border:1px solid var(--white);font-size:13px;letter-spacing:1px;display:flex;align-items:center;justify-content:center}

/* newsletter */
.news{left:0;top:2208px;width:1200px;height:139px;background:linear-gradient(100deg,#0b4f8c 0%,#0c7c9a 35%,#08a590 65%,#2fb27d 100%)}
.news-title{left:0;top:2231px;width:1200px;text-align:center;font-size:17px;letter-spacing:2px;color:var(--white)}
.news-sub{left:0;top:2259px;width:1200px;text-align:center;font-size:13px;color:var(--white)}
.field{top:2295px;width:296px;height:29px;border:1px solid rgba(255,255,255,.7);color:var(--white);font-size:10px;padding:9px 10px}
.subscribe{left:848px;top:2295px;width:122px;height:29px;background:var(--navy);color:var(--white);font-size:11px;letter-spacing:1px;display:flex;align-items:center;justify-content:center}

/* share */
.share-title{left:0;top:2374px;width:1200px;text-align:center;font-size:18px;letter-spacing:2px;color:#333}
.share-row{left:0;top:2422px;width:1200px;display:flex;justify-content:center;gap:18px;font-size:10px;color:#888}
.share-row span::before{content:"";display:inline-block;width:8px;height:8px;border-radius:50%;background:#666;margin-right:4px;vertical-align:-1px}

/* footer */
.foot-col{top:2487px}
.foot-col h4{font-size:12px;font-weight:400;letter-spacing:1.2px;color:#333;padding-bottom:5px;position:relative}
.foot-col h4::after{content:"";position:absolute;left:0;bottom:0;width:30px;height:1px;background:#333}
.foot-col ul{list-style:none;margin-top:9px}
.foot-col li{font-size:10px;line-height:18px;color:#666}
.foot-band{left:0;top:2628px;width:1200px;height:51px;background:var(--foot-band);display:flex;align-items:center;justify-content:center;font-size:15px;color:#444}
.copyright{left:0;top:2679px;width:1200px;height:40px;background:var(--foot-dark);display:flex;align-items:center;justify-content:center;font-size:10px;color:#ddd}
</style>
</head>
<body>
<div class="page">

  <header class="header abs">
    <div class="call abs">CALL: 020 7946 0185</div>
    <div class="mail abs">MAIL: hello@lumengetaways.example</div>
    <div class="brand abs"><span class="brand-mark"></span><span class="brand-name">LUMEN GETAWAYS</span></div>
    <svg class="search abs" width="16" height="16" viewBox="0 0 16 16" aria-label="Search"><circle cx="6.5" cy="6.5" r="4.8" fill="none" stroke="#222" stroke-width="2"/><line x1="10" y1="10" x2="14.5" y2="14.5" stroke="#222" stroke-width="2.2"/></svg>
    <div class="login abs">➜ LOG-IN</div>
    <div class="socials abs"><span></span><span></span><span></span><span></span><span></span></div>
  </header>

  <nav class="nav abs">
    <span class="caret">DESTINATIONS</span>
    <span class="caret">EXPERIENCES</span>
    <span class="caret">TRIPS BY MONTH</span>
    <span>TOPICAL NOW</span>
    <span>TAILORED</span>
    <span>PIONEERS CLUB</span>
    <span>BLOGS &amp; REVIEWS</span>
  </nav>

  <section class="hero abs" role="img" aria-label="Three hikers walking along a rocky ridge above a mountain lake with snowy peaks"></section>
  <h1 class="hero-title abs">Once-in-a-Lifetime Experiences in Less Than <b>7 Days</b></h1>
  <p class="hero-sub abs">Spectacular Hiking, Climbing &amp; Walking</p>
  <div class="hero-btn abs">Look, Book &amp; Go</div>

  <p class="intro-kicker abs">TOO BUSY TO RESEARCH AND BOOK A TRIP?</p>
  <h2 class="intro-title abs">CHOOSE OUR PRE-PACKAGED TRIPS WITH AN EASY 'LOOK AND BOOK' CONCEPT</h2>
  <p class="intro-text abs">Maximum Experiences in the Minimum Time Necessary to Enjoy. Can be Taken in a Weekend, Long-Weekend, or for Further Away or More Involved Experiences, up to One Working Week.</p>
  <div class="intro-down abs"><svg width="10" height="8" viewBox="0 0 10 8"><path d="M1 2l4 4 4-4" fill="none" stroke="#333" stroke-width="1.4"/></svg></div>

  <div class="tile abs" style="left:161px;top:866px"><div class="tile-img" role="img" aria-label="Mountain gorilla in green forest" style="background:linear-gradient(135deg,#2d3a1e,#1b1b18 55%,#4d6b22)"></div><div class="tile-cap"><small>Wonders</small><span>of Wildlife</span></div></div>
  <div class="tile abs" style="left:388px;top:866px"><div class="tile-img" role="img" aria-label="Colour festival crowd covered in bright powder" style="background:linear-gradient(135deg,#c2357a,#e1872a 45%,#6a3fa0)"></div><div class="tile-cap"><small>World's</small><span>Greatest Festivals</span></div></div>
  <div class="tile abs" style="left:613px;top:866px"><div class="tile-img" role="img" aria-label="Kayakers paddling through white water rapids" style="background:linear-gradient(180deg,#2a6fa3,#c9dbe6 55%,#4d88b0)"></div><div class="tile-cap"><small>Must Do</small><span>Activities</span></div></div>
  <div class="tile abs" style="left:837px;top:866px"><div class="tile-img" role="img" aria-label="Hot air balloons launching over a field" style="background:linear-gradient(180deg,#c9dcec,#d96a3c 50%,#6f8a3a)"></div><div class="tile-cap"><small>Unique</small><span>Annual Events</span></div></div>

  <div class="tile abs" style="left:161px;top:1073px"><div class="tile-img" role="img" aria-label="Sunlit sea cave with turquoise water" style="background:linear-gradient(180deg,#1b3a2c,#2f8c86 55%,#10302a)"></div><div class="tile-cap"><small>Extraordinary &amp;</small><span>Secret Places</span></div></div>
  <div class="tile abs" style="left:388px;top:1073px"><div class="tile-img" role="img" aria-label="Dancer in a flowing pink dress on a dark stage" style="background:linear-gradient(135deg,#111,#c8236a 50%,#1a1a1a)"></div><div class="tile-cap"><small>Unforgettable</small><span>Performances</span></div></div>
  <div class="tile abs" style="left:613px;top:1073px"><div class="tile-img" role="img" aria-label="Climbers on a rocky summit" style="background:linear-gradient(180deg,#9fb2c4,#6d7378 55%,#3a3c3e)"></div><div class="tile-cap"><small>Spectacular Hiking,</small><span>Climbing &amp; Walking</span></div></div>
  <div class="tile abs" style="left:837px;top:1073px"><div class="tile-img" role="img" aria-label="Colourful hilltop palace under a blue sky" style="background:linear-gradient(180deg,#4f8fd0,#e0b43a 55%,#b8583a)"></div><div class="tile-cap"><small>Private Castles,</small><span>Chateaux &amp; Paradors</span></div></div>

  <div class="feature-band abs"></div>
  <section class="feature abs"></section>
  <h3 class="feature-title abs">LOREM IPSUM DOLOR SIT AMET</h3>
  <p class="feature-text abs">Lorem ipsum dolor sit amet, consect etuer adipi-scing elaesen t vestibulum olestie lacus. Aenean nonummy hendrerit mauris.</p>
  <div class="video abs" role="img" aria-label="Video still of a helicopter flying over a tropical reef lagoon"></div>
  <svg class="play abs" width="68" height="68" viewBox="0 0 68 68" aria-label="Play video"><circle cx="34" cy="34" r="31" fill="rgba(0,0,0,.35)" stroke="#fff" stroke-width="3"/><path d="M27 21l20 13-20 13z" fill="#fff"/></svg>
  <div class="dots abs"><span class="on"></span><span></span><span></span><span></span><span></span></div>

  <section class="abs" style="left:0;top:1735px;width:1200px;height:473px;background:var(--band)"></section>
  <h2 class="offers-title abs">FEATURED OFFERS</h2>
  <article class="offer abs" style="left:161px" role="img" aria-label="Venice carnival mask">
    <div style="position:absolute;inset:0;background:linear-gradient(135deg,#e0a23a,#c23b22 50%,#e9d7c7)"></div>
    <div class="offer-frame"><h3>Venice Carnival</h3><p>£599pp</p><div class="offer-btn">BOOK NOW</div></div>
  </article>
  <article class="offer abs" style="left:460px" role="img" aria-label="Stone statues on Easter Island under blue sky">
    <div style="position:absolute;inset:0;background:linear-gradient(180deg,#4a86c8,#7fa6cf 45%,#5a5347 70%,#6e8a3a)"></div>
    <div class="offer-frame"><h3>Easter Island</h3><p>£2999pp</p><div class="offer-btn">BOOK NOW</div></div>
  </article>
  <article class="offer abs" style="left:761px" role="img" aria-label="Red rock butte on the Pacific Crest Trail">
    <div style="position:absolute;inset:0;background:linear-gradient(180deg,#a9b4c0,#8b6a57 40%,#9b3d22 70%,#6b2b18)"></div>
    <div class="offer-frame"><h3>Pacific Crest Trail</h3><p>£599pp</p><div class="offer-btn">BOOK NOW</div></div>
  </article>

  <section class="news abs"></section>
  <h2 class="news-title abs">SIGNUP FOR OUR NEWSLETTER</h2>
  <p class="news-sub abs">Receive news and offers from LG</p>
  <div class="field abs" style="left:230px">Your Full Name</div>
  <div class="field abs" style="left:538px">Email Address</div>
  <div class="subscribe abs">SUBSCRIBE</div>

  <h2 class="share-title abs">SHARE US</h2>
  <div class="share-row abs"><span>Circlepage</span><span>Chirpline</span><span>Pinwall</span><span>Snapframe</span><span>Streamtube</span></div>

  <div class="foot-col abs" style="left:169px"><h4>QUICK LINKS</h4><ul><li>Home</li><li>About</li><li>Contacts Us</li></ul></div>
  <div class="foot-col abs" style="left:352px"><h4>RESOURCES</h4><ul><li>Our Partner</li><li>Careers with LG</li><li>Press Room</li></ul></div>
  <div class="foot-col abs" style="left:567px"><h4>SUPPORT</h4><ul><li>Travel Advice</li><li>Financial Protection</li><li>Travel Insurance</li><li>FAQs</li><li>Contacts Us</li></ul></div>
  <div class="foot-col abs" style="left:720px"><h4>BOOKING</h4><ul><li>Booking Conditions</li><li>Group Bookings</li><li>Tailor-Made &amp; Extra Nights</li><li>Booking Flights</li></ul></div>
  <div class="foot-col abs" style="left:890px"><h4>INFORMATION</h4><ul><li>Visas</li><li>Terms of Use</li><li>Privacy &amp; Cookies</li></ul></div>

  <div class="foot-band abs">LG Protecting wildlife &amp; animals,and supporting local communities</div>
  <div class="copyright abs">Copyright 2017 www.lumengetaways.example All Rights Reserved.</div>
</div>
</body>
</html>
```